Design of Referral Card for Marlin Storage Group

Card Specifications:
- Size: 4x6 inches
- Format: Two-sided
- Design Style: Simple, eye-catching, and easy to read
CARD DETAILS:
1. Header:
- Main Brand Logo: Display the “Marlin Storage Group” logo prominently at the top center.
2. Referral Information:
- Text Fields:
- Referred By Name: [Blank space for name]
- Referred By Phone Number: [Blank space for phone number]
- Use a clean, legible font and ensure ample space for filling out the information.
3. Facility Logos and Addresses:
- Facility Logos: Include small logos/icons for each facility brand:
- True Harbor Self Storage
- Ned Cardle Self Storage
- Quillan Self Storage
- Ravensmoor Self Storage
- Facility Names and Addresses:
- True Harbor Self Storage: 2753 Quenby Road, Warner Robins, GA 31088
- Ned Cardle Self Storage: 418 Ashgrove Drive, Perry, GA 31069
- Quillan Self Storage:
- 392 N Parson Road, Byron, GA 31008
- 264 S T Halden Sr Pkwy, Byron, GA 31008
- 815 GA-83, Byron, GA 31008
- Ravensmoor Self Storage:
- 728 S Pellam Ridge Blvd, Centerville, GA 31028
- 476 Dorian Kesh Pkwy, Centerville, GA 31028
4. Important Notice:
- Text: “CARD MUST BE PRESENTED AT TIME OF RENTAL FOR DISCOUNT AND REFERRAL FEE DISTRIBUTION”
- Ensure this message is clear and stands out.
5. Website:
- Include the website URL: www.MarlinStorageGroup.example
- Position the website URL at the bottom or in a location that is easy to find.
OTHER DETAILS:
1. Facility Details:
- Organize the addresses for each facility in a clean and easy-to-read format. Use small icons or logos next to each address for visual clarity.
2. Design Elements:
- Layout: Ensure a balanced layout with sufficient space around text and logos to avoid clutter.
- Colors: Use a color scheme that aligns with the brand’s visual identity, maintaining a cohesive look with the front side.
Attachments:
- Marlin Storage Group Logo
- Facility Logos (True Harbor, Ned Cardle, Byron, Centerville)
Objective:
Design a visually appealing referral card that effectively communicates necessary information, including referral details, facility addresses, and important instructions. Ensure the card is simple yet striking, with clear and accessible information for users.
Target Market(s)
People looking for extra space to store their belongings
Industry/Entity Type
Self-Storage

```html
<!DOCTYPE html>
<html lang="en">
<head>
<meta charset="utf-8">
<title>Marlin Storage Group – Referral Card</title>
<link href="https://fonts.googleapis.com/css2?family=Oswald:wght@500;600;700&family=Montserrat:wght@500;600&display=swap" rel="stylesheet">
<style>
  :root{
    --stage:#4b4b4d;
    --card:#ffffff;
    --navy:#1d2a4d;
    --sky:#27a6e1;
    --ink:#1f2433;
    --rule:#8a8f99;
    --steel-light:#eef0f3;
    --steel-mid:#c9ced6;
    --steel-dark:#6f7785;
  }
  *{box-sizing:border-box;margin:0;padding:0}
  html,body{width:1200px;height:2324px;overflow:hidden}
  body{background:var(--stage);position:relative;font-family:"Montserrat",sans-serif}

  .card{position:absolute;left:210px;width:780px;height:1100px;background:var(--card);overflow:hidden}
  .card--front{top:30px}
  .card--back{top:1192px}

  /* shared brand lockup */
  .brand{position:absolute;left:0;right:0;top:110px;display:flex;align-items:center;justify-content:center;gap:22px}
  .brand__mark{width:58px;height:58px;background:var(--navy)}
  .brand__name{font-family:"Oswald",sans-serif;font-weight:700;font-size:60px;letter-spacing:2px;color:var(--navy);text-transform:uppercase;line-height:1}
  .brand-rule{position:absolute;top:214px;left:170px;right:170px;height:4px;background:var(--sky)}

  /* front */
  .front__photo{position:absolute;left:0;top:0;width:780px;height:560px;
    background:linear-gradient(180deg,rgba(255,255,255,.2),#fff 95%),
               linear-gradient(90deg,var(--steel-mid),var(--steel-light) 45%,var(--steel-light) 55%,var(--steel-mid));}
  .referral{position:absolute;left:76px;right:76px;top:412px}
  .referral__row{display:flex;align-items:flex-end;gap:14px;margin-bottom:22px}
  .referral__label{font-family:"Oswald",sans-serif;font-weight:600;font-size:27px;color:var(--ink);letter-spacing:.5px;white-space:nowrap}
  .referral__line{flex:1;border-bottom:2px solid var(--ink);margin-bottom:6px}

  .facilities{position:absolute;left:0;right:0;top:566px;height:484px}
  .facilities__band{position:absolute;left:272px;right:0;top:0;bottom:0;background:var(--sky)}
  .facility{position:absolute;left:0;right:0;display:flex;align-items:center}
  .facility + .facility{border-top:2px solid rgba(255,255,255,.8)}
  .facility__name{width:272px;padding:0 18px;text-align:center;font-family:"Oswald",sans-serif;font-weight:600;font-size:20px;line-height:1.15;color:var(--navy);text-transform:uppercase}
  .facility__addresses{padding-left:40px;color:#fff;font-size:17px;font-weight:500;line-height:1.5}
  .facility--1{top:0;height:120px}
  .facility--2{top:120px;height:96px}
  .facility--3{top:216px;height:144px}
  .facility--4{top:360px;height:124px}
  .facility--1 .facility__name,.facility--2 .facility__name,.facility--3 .facility__name,.facility--4 .facility__name{border:none}

  .front__footer{position:absolute;left:0;bottom:40px;height:16px;width:780px;display:flex}
  .front__footer-navy{width:600px;background:var(--navy)}
  .front__footer-sky{flex:1;background:var(--sky)}

  /* back */
  .back__photo{position:absolute;left:32px;top:320px;width:716px;height:752px;
    background:linear-gradient(180deg,#f3f4f6 0%,var(--steel-mid) 40%,var(--steel-dark) 100%);}
  .notice{position:absolute;left:64px;top:568px;width:652px;height:320px;background:rgba(29,42,77,.88);
    display:flex;align-items:center;justify-content:center;padding:0 56px}
  .notice__text{font-family:"Oswald",sans-serif;font-weight:600;font-size:36px;line-height:1.3;color:#fff;text-align:center;letter-spacing:1px;text-transform:uppercase}
  .website{position:absolute;left:64px;top:944px;width:652px;height:80px;background:var(--navy);
    display:flex;align-items:center;justify-content:center}
  .website__url{font-family:"Montserrat",sans-serif;font-weight:500;font-size:25px;color:#fff;letter-spacing:1.5px}
</style>
</head>
<body>

<section class="card card--front">
  <div class="front__photo" role="img" aria-label="Faded photo of a self-storage corridor with roll-up unit doors"></div>

  <div class="brand">
    <span class="brand__mark"></span>
    <span class="brand__name">Marlin Storage Group</span>
  </div>
  <div class="brand-rule"></div>

  <div class="referral">
    <div class="referral__row"><span class="referral__label">REFERRED BY NAME:</span><span class="referral__line"></span></div>
    <div class="referral__row"><span class="referral__label">REFERRED BY PHONE NUMBER:</span><span class="referral__line"></span></div>
  </div>

  <div class="facilities">
    <div class="facilities__band"></div>
    <div class="facility facility--1">
      <div class="facility__name">True Harbor</div>
      <div class="facility__addresses">2753 Quenby Road, Warner Robins, GA 31088</div>
    </div>
    <div class="facility facility--2">
      <div class="facility__name">Ned Cardle</div>
      <div class="facility__addresses">418 Ashgrove Drive, Perry, GA 31069</div>
    </div>
    <div class="facility facility--3">
      <div class="facility__name">Quillan</div>
      <div class="facility__addresses">392 N Parson Road, Byron, GA 31008<br>264 S T Halden Sr Pkwy, Byron, GA 31008<br>815 GA-83, Byron, GA 31008</div>
    </div>
    <div class="facility facility--4">
      <div class="facility__name">Ravensmoor</div>
      <div class="facility__addresses">728 S Pellam Ridge Blvd, Centerville, GA 31028<br>476 Dorian Kesh Pkwy, Centerville, GA 31028</div>
    </div>
  </div>

  <div class="front__footer"><span class="front__footer-navy"></span><span class="front__footer-sky"></span></div>
</section>

<section class="card card--back">
  <div class="brand">
    <span class="brand__mark"></span>
    <span class="brand__name">Marlin Storage Group</span>
  </div>
  <div class="brand-rule"></div>

  <div class="back__photo" role="img" aria-label="Photo of an indoor storage hallway with unit doors and a moving cart"></div>

  <div class="notice">
    <p class="notice__text">Card must be presented at time of rental for discount and referral fee distribution</p>
  </div>

  <div class="website"><span class="website__url">www.MarlinStorageGroup.example</span></div>
</section>

</body>
</html>
```